Machine Sign

This is for a laundromat. I would like signs to hang above the machines from the ceiling indicating machine size. For example we have 6 loaders, 4 loaders, 2 loaders.

```html
<!DOCTYPE html>
<html lang="en">
<head>
<meta charset="utf-8">
<title>Machine Size Signs</title>
<link href="https://fonts.googleapis.com/css2?family=Montserrat:wght@700;800&display=swap" rel="stylesheet">
<style>
  :root {
    --backdrop: #f3e4bd;
    --sign-white: #ffffff;
    --sign-peach: #f6bd84;
    --teal: #189794;
    --shadow: #a39376;
  }
  html, body {
    margin: 0;
    padding: 0;
    width: 1200px;
    height: 436px;
    overflow: hidden;
    background: var(--backdrop);
  }
  .sign-row {
    position: relative;
    width: 1200px;
    height: 436px;
  }
  .sign {
    position: absolute;
    top: 45px;
    width: 334px;
    height: 334px;
    background: var(--sign-white);
    box-shadow: 5px 5px 0 var(--shadow);
    overflow: hidden;
  }
  .sign--six { left: 69px; }
  .sign--four { left: 432px; }
  .sign--two { left: 797px; }
  .sign__arcs {
    position: absolute;
    left: 0;
    top: 0;
    width: 334px;
    height: 163px;
  }
  .sign__band {
    position: absolute;
    left: 0;
    top: 163px;
    width: 334px;
    height: 171px;
    background: var(--sign-peach);
  }
  .sign__count {
    position: absolute;
    left: 0;
    width: 334px;
    top: 100px;
    margin: 0;
    text-align: center;
    font-family: "Montserrat", sans-serif;
    font-weight: 800;
    font-size: 128px;
    line-height: 130px;
    color: var(--teal);
  }
  .sign__label {
    position: absolute;
    left: 0;
    width: 334px;
    top: 216px;
    margin: 0;
    text-align: center;
    font-family: "Montserrat", sans-serif;
    font-weight: 700;
    font-size: 37px;
    line-height: 40px;
    letter-spacing: 0.2em;
    text-indent: 0.2em;
    color: var(--teal);
  }
  .sign__machine {
    position: absolute;
    left: 136px;
    top: 258px;
    width: 62px;
    height: 62px;
    background: rgba(24, 151, 148, 0.18);
  }
</style>
</head>
<body>
  <main class="sign-row">
    <section class="sign sign--six">
      <svg class="sign__arcs" viewBox="0 0 334 163" aria-hidden="true">
        <circle cx="167" cy="168" r="83" fill="none" stroke="var(--teal)" stroke-width="1.4"/>
        <circle cx="167" cy="168" r="73.5" fill="none" stroke="var(--teal)" stroke-width="2.8"/>
      </svg>
      <div class="sign__band"></div>
      <p class="sign__count">6</p>
      <p class="sign__label">LOADERS</p>
      <div class="sign__machine" role="img" aria-label="Line icon of a front-loading washing machine"></div>
    </section>
    <section class="sign sign--four">
      <svg class="sign__arcs" viewBox="0 0 334 163" aria-hidden="true">
        <circle cx="167" cy="168" r="83" fill="none" stroke="var(--teal)" stroke-width="1.4"/>
        <circle cx="167" cy="168" r="73.5" fill="none" stroke="var(--teal)" stroke-width="2.8"/>
      </svg>
      <div class="sign__band"></div>
      <p class="sign__count">4</p>
      <p class="sign__label">LOADERS</p>
      <div class="sign__machine" role="img" aria-label="Line icon of a front-loading washing machine"></div>
    </section>
    <section class="sign sign--two">
      <svg class="sign__arcs" viewBox="0 0 334 163" aria-hidden="true">
        <circle cx="167" cy="168" r="83" fill="none" stroke="var(--teal)" stroke-width="1.4"/>
        <circle cx="167" cy="168" r="73.5" fill="none" stroke="var(--teal)" stroke-width="2.8"/>
      </svg>
      <div class="sign__band"></div>
      <p class="sign__count">2</p>
      <p class="sign__label">LOADERS</p>
      <div class="sign__machine" role="img" aria-label="Line icon of a front-loading washing machine"></div>
    </section>
  </main>
</body>
</html>
```